Ledgerline Systems Group business card design.

We are a software development company that develop Software for finance companies and related industries.

We need a 2 sided business card designed. We have a new logo already designed (see attached eps and ai) We are after a clean simple corporate look. One side with just our logo, and the second side with our details.

Marcus Thelwell
Managing Director

Suite 4 Level 9, 318 Harbin Lane Sydney NSW 2000

Direct: +61 2 9478 3062
Mobile: +61 4 1237 6845
Email: marcust@lsg.net.au
Web: www.lsg.net.au

I have included 2 logo files an .ai and .eps. I noticed that the lines either side of the partners looks a bit jaggered and needs to be made sharper.

I would like to introduce a little colour somewhere rather than having it all black and white. But not over the top, keeping with a simple clean corporate look. Perhaps a light blue on some of the text?

If you have other ideas would be pleased to review

Regards

Marcus T.

```html
<!DOCTYPE html>
<html lang="en">
<head>
<meta charset="utf-8">
<title>Ledgerline Systems Group — Business Card</title>
<link rel="stylesheet" href="https://fonts.googleapis.com/css2?family=Open+Sans:wght@400;600;700&display=swap">
<style>
  :root {
    --backdrop: #322c29;
    --card-black: #141212;
    --card-white: #f7f7f6;
    --ink: #111111;
    --ink-muted: #9a9a9a;
    --ink-body: #2a2a2a;
    --icon: #8c8c8c;
    --paper-text: #ffffff;
  }
  * { box-sizing: border-box; margin: 0; padding: 0; }
  html, body {
    width: 1200px; height: 768px; overflow: hidden;
    background: var(--backdrop);
    font-family: "Open Sans", Arial, sans-serif;
  }
  .stage {
    position: relative; width: 1200px; height: 768px;
    display: flex; align-items: center; justify-content: center; gap: 48px;
  }
  .card {
    width: 520px; height: 318px; border-radius: 3px;
    position: relative; overflow: hidden;
    box-shadow: 0 10px 30px rgba(0,0,0,.45);
  }
  /* Front side */
  .card--front {
    background: var(--card-black);
    display: flex; flex-direction: column; align-items: center; justify-content: center;
  }
  .brand-front {
    display: flex; align-items: center; gap: 14px;
    color: var(--paper-text);
    font-weight: 700; font-size: 24px; letter-spacing: .06em; text-transform: uppercase;
  }
  .brand-front__mark {
    width: 22px; height: 22px; background: var(--paper-text);
  }
  /* Back side */
  .card--back {
    background: var(--card-white);
    display: grid; grid-template-columns: 220px 1fr; align-items: center;
    padding: 0 30px 0 34px;
  }
  .brand-back {
    display: flex; align-items: center; gap: 12px;
    color: var(--ink); font-weight: 700; font-size: 19px; line-height: 1.15;
    text-transform: uppercase; letter-spacing: .03em;
  }
  .brand-back__mark {
    flex: none; width: 34px; height: 34px; background: var(--ink);
  }
  .details { padding-left: 22px; color: var(--ink-body); font-size: 12.5px; line-height: 1.45; }
  .details__name { font-weight: 700; font-size: 15px; color: var(--ink); }
  .details__role { color: var(--ink-muted); font-size: 11px; margin-bottom: 14px; }
  .details__address { margin-bottom: 12px; }
  .contact-list { list-style: none; }
  .contact-list li { display: flex; align-items: center; gap: 9px; }
  .contact-list svg { width: 10px; height: 10px; fill: var(--icon); flex: none; }
</style>
</head>
<body>
<main class="stage">
  <section class="card card--front" aria-label="Card front">
    <div class="brand-front">
      <span class="brand-front__mark" aria-hidden="true"></span>
      <span>Ledgerline Systems Group</span>
    </div>
  </section>

  <section class="card card--back" aria-label="Card back">
    <div class="brand-back">
      <span class="brand-back__mark" aria-hidden="true"></span>
      <span>Ledgerline<br>Systems<br>Group</span>
    </div>
    <div class="details">
      <p class="details__name">Marcus Thelwell</p>
      <p class="details__role">Managing Director</p>
      <p class="details__address">Suite 4 Level 9, 318 Harbin Lane<br>Sydney NSW 2000</p>
      <ul class="contact-list">
        <li>
          <svg viewBox="0 0 10 10" aria-hidden="true"><path d="M1 3.5C1 2 2 1 3.5 1h3C8 1 9 2 9 3.5v1H7V3.5H3v1H1z M2 5h6l1 4H1z"/></svg>
          +61 2 9478 3062
        </li>
        <li>
          <svg viewBox="0 0 10 10" aria-hidden="true"><path d="M3 0h4a1 1 0 0 1 1 1v8a1 1 0 0 1-1 1H3a1 1 0 0 1-1-1V1a1 1 0 0 1 1-1zm0 1.5v6h4v-6z"/></svg>
          +61 4 1237 6845
        </li>
        <li>
          <svg viewBox="0 0 10 10" aria-hidden="true"><path d="M0 2h10v.8L5 6 0 2.8z M0 3.9l5 3.2 5-3.2V8H0z"/></svg>
          marcust@lsg.net.au
        </li>
        <li>
          <svg viewBox="0 0 10 10" aria-hidden="true"><circle cx="5" cy="5" r="4.5"/></svg>
          www.lsg.net.au
        </li>
      </ul>
    </div>
  </section>
</main>
</body>
</html>
```